Plakate für Kirchenmusik-Jubiläen
Es war wirklich eine tolle Zusammenarbeit! Während des Projektes war es sehr unkompliziert und auch nach Abschluss des Projektes, nachdem der Gewinner gekürt wurde, waren Änderungen problemlos möglich. Ein äußerst freundlicher und kompetenter Designer!
Zielgruppe
Wir sind eine Kirchengemeinde (St. Ansgar in Gifhorn, Niedersachsen), die in diesem Jahr sechs Jubiläen feiert (siehe unten).
Es finden dafür Jubiläumswochen statt, vom 23.6. bis 9.7.. In diesen Wochen finden mehrere Veranstaltungen statt. Die Zielgruppen sind grundsätzlich an alle, aber sicherlich treffen die Veranstaltungen den Geschmack von Interessierten und allen Menschen über 50+.
Aufgabenstellung
Überschrift ist: Jubiläumswochen St. Ansgar
Ich bräuchte ein hochkant Format in DIN A3, und DIN A2.
Ich hätte gerne folgendende Texte, die unbedingt vorkommen sollen:
275 Jahre Gottlieb Renner Orgel, 120 Jahre Kantorei, 90 Jahre Posaunenchor, 25 Jahre Abendmusik am Burggraben, 25 Jahre Freundeskreis, 10 Jahre Ruhepunkt am Mittag.
23.06.2023 19.00 Uhr Eröffnungskonzert vom Freundeskreis - mit dem Streichquintett des Kammermusikensembles Wolfsried, Eintritt: 12,- / 8,- (erm.), nur Abendkasse
24.06.2023 17.00 Uhr Kinderchorkonzert - mit Schulchören Birkenfelde und Moorhausen, Kinderchor St. Ansgar und 'Blech Quartett'
02.07.2023 17.00 Uhr Abendmusik am Burggraben - mit Posaunenchor und Kantorei
06.07.2023 ab 10 Uhr Orgelkurs zum Ferienbeginn - für Anfänger und Fortgeschrittene
09.07.2023 20.00-24.00 Uhr Orgelnacht - mit Snacks und Getränken in den Pausen
Nähere Informationen unter www.ansgar-gemeinde.de
Ich lade noch ein Logo hoch, das auch plaziert werden soll.

```html
<!DOCTYPE html>
<html lang="de">
<head>
<meta charset="utf-8">
<title>Jubiläumswochen St. Ansgar</title>
<link href="https://fonts.googleapis.com/css2?family=Playfair+Display:ital,wght@1,500&family=Source+Serif+4:opsz,wght@8..60,400;8..60,700&display=swap" rel="stylesheet">
<style>
  :root {
    --red: #a51d21;
    --gold: #c9aa14;
    --panel: #ebebeb;
    --ink: #1a1a1a;
    --white: #ffffff;
  }
  * { margin: 0; padding: 0; box-sizing: border-box; }
  html, body { width: 849px; height: 1200px; overflow: hidden; background: var(--panel); }
  .poster {
    position: relative; width: 849px; height: 1200px; overflow: hidden;
    background: var(--panel);
    font-family: "Source Serif 4", Georgia, serif;
    font-variant-numeric: oldstyle-nums;
    color: var(--ink);
  }
  .top-rule { position: absolute; left: 0; top: 0; width: 100%; height: 5px; background: var(--red); z-index: 3; }
  .hero-photo {
    position: absolute; left: 0; top: 0; width: 849px; height: 433px;
    background: linear-gradient(120deg, #6e5446 0%, #9a7460 30%, #c4a08a 55%, #b58f7c 75%, #d8c2b4 100%);
  }
  .title-box {
    position: absolute; left: 246px; top: 33px; width: 603px; height: 154px;
    background: rgba(255,255,255,0.88); border-radius: 6px 0 0 6px;
    font-family: "Playfair Display", Georgia, serif; font-style: italic; font-weight: 500;
    color: #111; font-size: 66px; line-height: 72px;
  }
  .title-box .line1 { position: absolute; left: 20px; top: 42px; transform: translateY(-50%); white-space: nowrap; }
  .title-box .line2 { position: absolute; left: 103px; top: 116px; transform: translateY(-50%); white-space: nowrap; }
  .parish-mark {
    position: absolute; left: 60px; top: 170px; width: 220px; text-align: center;
    color: var(--red); font-weight: 700; font-size: 30px; line-height: 36px;
  }
  .parish-mark .dot { display: block; width: 34px; height: 34px; margin: 0 auto 10px; border-radius: 50%; background: var(--red); }
  .info-panel { position: absolute; left: 320px; top: 213px; width: 529px; height: 904px; background: var(--panel); }
  .jubilee-card {
    position: absolute; left: 40px; top: 381px; width: 271px; height: 736px;
    background: var(--white); border-radius: 6px 6px 0 0;
    color: var(--red); text-align: center;
  }
  .jubilee { position: absolute; left: 0; width: 100%; }
  .jubilee .years { font-size: 31px; line-height: 40px; }
  .jubilee .name { font-size: 26px; line-height: 38px; }
  .event { position: absolute; left: 349px; width: 490px; }
  .event .when { position: relative; height: 30px; font-weight: 700; font-size: 27px; line-height: 30px; }
  .event .when .date { letter-spacing: 2.5px; }
  .event .when .time { position: absolute; left: 231px; top: 0; white-space: nowrap; font-size: 25px; letter-spacing: 0; }
  .event .what { font-weight: 700; font-size: 25.5px; line-height: 38px; white-space: nowrap; }
  .event .detail { font-size: 20.5px; line-height: 26px; white-space: nowrap; }
  .event .detail.gap { margin-top: 4px; }
  .divider { position: absolute; left: 336px; width: 466px; height: 6px; }
  .footer {
    position: absolute; left: 0; top: 1117px; width: 849px; height: 83px;
    background: var(--gold); text-align: center;
    font-size: 19.5px; line-height: 83px; color: var(--ink);
  }
</style>
</head>
<body>
<div class="poster">
  <div class="top-rule"></div>
  <div class="hero-photo" role="img" aria-label="Nahaufnahme einer Violine mit Saiten in warmen Brauntönen"></div>

  <div class="title-box">
    <div class="line1">Jubiläumswochen</div>
    <div class="line2">St. Ansgar</div>
  </div>

  <div class="parish-mark"><span class="dot"></span>St. Ansgar</div>

  <div class="info-panel"></div>

  <div class="jubilee-card">
    <div class="jubilee" style="top:23px"><div class="years">275 Jahre</div><div class="name">Gottlieb Renner Orgel</div></div>
    <div class="jubilee" style="top:129px"><div class="years">120 Jahre</div><div class="name">Kantorei</div></div>
    <div class="jubilee" style="top:235px"><div class="years">90 Jahre</div><div class="name">Posaunenchor</div></div>
    <div class="jubilee" style="top:339px"><div class="years">25 Jahre</div><div class="name">Abendmusik am<br>Burggraben</div></div>
    <div class="jubilee" style="top:480px"><div class="years">25 Jahre</div><div class="name">Freundeskreis</div></div>
    <div class="jubilee" style="top:583px"><div class="years">10 Jahre</div><div class="name">Ruhepunkt am<br>Mittag</div></div>
  </div>

  <div class="event" style="top:252px">
    <div class="when"><span class="date">23.06.2023</span><span class="time">19.00 Uhr</span></div>
    <div class="what">Eröffnungskonzert vom Freundeskreis</div>
    <div class="detail">mit dem Streichquintett</div>
    <div class="detail">des Kammermusikensembles Wolfsried</div>
    <div class="detail gap">Eintritt: 12,- / 8,-&nbsp; (erm.),</div>
    <div class="detail">nur Abendkasse</div>
  </div>
  <svg class="divider" style="top:443px" viewBox="0 0 466 6"><line x1="3" y1="3" x2="463" y2="3" stroke="var(--gold)" stroke-width="5.5" stroke-linecap="round" stroke-dasharray="0 17"/></svg>

  <div class="event" style="top:471px">
    <div class="when"><span class="date">24.06.2023</span><span class="time">17.00 Uhr</span></div>
    <div class="what">Kinderchorkonzert</div>
    <div class="detail">mit Schulchören Birkenfelde und Moorhausen,</div>
    <div class="detail">Kinderchor St. Ansgar und „Blech Quartett“</div>
  </div>
  <svg class="divider" style="top:614px" viewBox="0 0 466 6"><line x1="3" y1="3" x2="463" y2="3" stroke="var(--gold)" stroke-width="5.5" stroke-linecap="round" stroke-dasharray="0 17"/></svg>

  <div class="event" style="top:653px">
    <div class="when"><span class="date">2.07.2023</span><span class="time">17.00 Uhr</span></div>
    <div class="what">Abendmusik am Burggraben</div>
    <div class="detail">mit Posaunenchor und Kantorei</div>
  </div>
  <svg class="divider" style="top:771px" viewBox="0 0 466 6"><line x1="3" y1="3" x2="463" y2="3" stroke="var(--gold)" stroke-width="5.5" stroke-linecap="round" stroke-dasharray="0 17"/></svg>

  <div class="event" style="top:809px">
    <div class="when"><span class="date">6.07.2023</span><span class="time">ab 10 Uhr</span></div>
    <div class="what">Orgelkurs zum Ferienbeginn</div>
    <div class="detail">für Anfänger und Fortgeschrittene</div>
  </div>
  <svg class="divider" style="top:924px" viewBox="0 0 466 6"><line x1="3" y1="3" x2="463" y2="3" stroke="var(--gold)" stroke-width="5.5" stroke-linecap="round" stroke-dasharray="0 17"/></svg>

  <div class="event" style="top:966px">
    <div class="when"><span class="date">9.07.2023</span><span class="time">20.00 - 24.00 Uhr</span></div>
    <div class="what">Orgelnacht</div>
    <div class="detail">Snacks und Getränke in Pausen</div>
  </div>
  <svg class="divider" style="top:1078px" viewBox="0 0 466 6"><line x1="3" y1="3" x2="463" y2="3" stroke="var(--gold)" stroke-width="5.5" stroke-linecap="round" stroke-dasharray="0 17"/></svg>

  <div class="footer">Nähere Informationen unter&nbsp; www.ansgar-gemeinde.de</div>
</div>
</body>
</html>
```